ultra-minimalist business card

front (black background, matte):

tarik b. hosseny
writer | photographer
get@tarikhosseny.com

back (white background, matte):

a picture speaks a thousand words;
a word draws a thousand pictures.

www.tarikhosseny.com

all text should be small (white or silver - as long as it shows against the black - on the front; black or gray - as long as it shows against the white - on the back).

feel free to get creative in terms of arrangement, alignment, and font type, but remember, the overall style is minimalist, so nothing too fancy, please.

thanks.

```html
<!DOCTYPE html>
<html lang="en">
<head>
<meta charset="utf-8">
<title>Tarik B. Hosseny — Business Card</title>
<link rel="stylesheet" href="https://fonts.googleapis.com/css2?family=Cinzel:wght@400;500&display=swap">
<style>
  :root {
    --stage: #1c1c1d;
    --card-front: #1f1f20;
    --card-back: #f7f7f5;
    --foil: #b88a45;
    --ink: #2a2a2a;
    --ink-soft: #4a4a4a;
  }
  * { box-sizing: border-box; margin: 0; padding: 0; }
  html, body {
    width: 1200px;
    height: 694px;
    overflow: hidden;
    background: var(--stage);
  }
  .sheet {
    width: 1200px;
    height: 694px;
    display: flex;
    align-items: center;
    justify-content: center;
    gap: 80px;
  }
  .card {
    width: 480px;
    height: 274px;
    border-radius: 3px;
    font-family: "Cinzel", "Times New Roman", serif;
    text-transform: uppercase;
    display: flex;
    flex-direction: column;
  }
  .card--front {
    background: var(--card-front);
    color: var(--foil);
    justify-content: center;
    padding-left: 62px;
    box-shadow: 0 0 0 1px rgba(255,255,255,0.04);
  }
  .card__name {
    font-size: 21px;
    font-weight: 500;
    letter-spacing: 0.12em;
    margin-bottom: 22px;
  }
  .card__role,
  .card__email {
    font-size: 12px;
    letter-spacing: 0.14em;
    line-height: 1.7;
  }
  .card--back {
    background: var(--card-back);
    color: var(--ink);
    align-items: center;
    justify-content: center;
    text-align: center;
  }
  .card__quote {
    font-size: 14px;
    letter-spacing: 0.08em;
    line-height: 1.45;
    margin-bottom: 40px;
  }
  .card__web {
    font-size: 11px;
    letter-spacing: 0.12em;
    color: var(--ink-soft);
  }
</style>
</head>
<body>
  <main class="sheet">
    <section class="card card--front" aria-label="Card front">
      <p class="card__name">tarik b. hosseny</p>
      <p class="card__role">writer | photographer</p>
      <p class="card__email">get@tarikhosseny.com</p>
    </section>
    <section class="card card--back" aria-label="Card back">
      <p class="card__quote">a picture speaks a thousand words;<br>a word draws a thousand pictures.</p>
      <p class="card__web">www.tarikhosseny.com</p>
    </section>
  </main>
</body>
</html>
```